Business Card design for new private practice opening

I need a business card design for my new private practice with my new logo uploaded as a file
On the front the logo
On the back: maybe a small logo somewhere?
Priv. Doz. DDr. Corinna Vestaluk
Fachärztin für Allgemein- & Viszeralchirurgie
Address: xxx
Tel: xxx
Mobil:xxx
Webseite:xxx
Email:xxx

Contact Information for Business Card

See project description above for details

Requirements
Nice to have
• I would like the colors of the logo incorporated into the business card

```html
<!DOCTYPE html>
<html lang="de">
<head>
<meta charset="utf-8">
<title>Halvera Chirurgie – Visitenkarte</title>
<link rel="stylesheet" href="https://fonts.googleapis.com/css2?family=Montserrat:wght@500;600;700&family=Figtree:wght@400&display=swap">
<style>
  :root {
    --backdrop: #353334;
    --teal: #46aca9;
    --teal-bright: #45bab7;
    --grey: #8a8a8a;
    --white: #ffffff;
  }
  * { margin: 0; padding: 0; box-sizing: border-box; }
  html, body {
    width: 1200px; height: 1176px; overflow: hidden;
    background: var(--backdrop);
  }
  .card {
    position: absolute; left: 222px; width: 756px; height: 432px; overflow: hidden;
  }
  .card-front { top: 141px; background: var(--teal); }
  .card-back { top: 603px; background: var(--white); }

  .brand { position: absolute; display: flex; align-items: center; }
  .brand-circle { border-radius: 50%; flex: none; }
  .brand-name {
    font-family: "Montserrat", sans-serif; font-weight: 700;
    text-transform: uppercase; line-height: 1; letter-spacing: 0.01em;
  }
  .card-front .brand { left: 170px; top: 154px; }
  .card-front .brand-circle { width: 124px; height: 124px; border: 4px solid var(--white); margin-right: 20px; }
  .card-front .brand-name { color: var(--white); font-size: 50px; }
  .card-front .brand-name span { display: block; }
  .card-front .brand-name span + span { margin-top: 14px; }

  .card-back .brand { left: 80px; top: 199px; }
  .card-back .brand-circle { width: 72px; height: 72px; border: 3px solid var(--grey); margin-right: 11px; }
  .card-back .brand-name { color: var(--grey); font-size: 28px; }
  .card-back .brand-name span { display: block; }
  .card-back .brand-name span + span { margin-top: 4px; }

  .divider {
    position: absolute; left: 352px; top: 151px; width: 2px; height: 167px;
    background: var(--teal-bright); border-radius: 1px;
  }
  .person { position: absolute; left: 384px; top: 60px; }
  .person-name {
    font-family: "Montserrat", sans-serif; font-weight: 600;
    font-size: 24px; color: var(--teal-bright); line-height: 1.1;
  }
  .person-role {
    font-family: "Figtree", sans-serif; font-size: 19px;
    color: var(--grey); margin-top: 2px; letter-spacing: 0.01em;
  }
  .contacts { position: absolute; left: 380px; top: 167px; list-style: none; }
  .contact {
    display: flex; align-items: flex-start;
    font-family: "Figtree", sans-serif; font-size: 21px; color: var(--grey); line-height: 25px;
  }
  .contact + .contact { margin-top: 4px; }
  .contact svg { width: 24px; height: 24px; flex: none; margin-right: 7px; fill: var(--teal-bright); }
  .wave { position: absolute; left: 0; bottom: 0; width: 756px; height: 432px; }
</style>
</head>
<body>
  <section class="card card-front">
    <div class="brand">
      <div class="brand-circle"></div>
      <div class="brand-name"><span>Halvera</span><span>Chirurgie</span></div>
    </div>
  </section>

  <section class="card card-back">
    <svg class="wave" viewBox="0 0 756 432" aria-hidden="true">
      <path d="M0 370 C160 405 360 400 560 365 C650 350 715 336 756 339 L756 432 L0 432 Z" fill="var(--grey)"/>
      <path d="M0 380 C160 414 360 410 560 372 C650 354 710 336 756 342 L756 432 L0 432 Z" fill="var(--teal-bright)"/>
    </svg>

    <div class="person">
      <h1 class="person-name">DDr. Corinna VESTALUK</h1>
      <p class="person-role">MANAGING DIRECTOR</p>
    </div>

    <div class="brand">
      <div class="brand-circle"></div>
      <div class="brand-name"><span>Halvera</span><span>Chirurgie</span></div>
    </div>

    <div class="divider"></div>

    <ul class="contacts">
      <li class="contact">
        <svg viewBox="0 0 24 24"><path d="M12 1C7.6 1 4.5 4.2 4.5 8.4 4.5 13.6 12 23 12 23s7.5-9.4 7.5-14.6C19.5 4.2 16.4 1 12 1zm0 10.2a2.8 2.8 0 1 1 0-5.6 2.8 2.8 0 0 1 0 5.6z"/></svg>
        <span>2817 Lindenweg,<br>Emsdorf, Germany</span>
      </li>
      <li class="contact">
        <svg viewBox="0 0 24 24"><path d="M2 8c0-2 4-4 10-4s10 2 10 4v2h-5V8.5c-1.5-.6-3-.8-5-.8s-3.5.2-5 .8V10H2zM6 11h12l2 9H4zm6 2a3 3 0 1 0 0 6 3 3 0 0 0 0-6zm0 1.5a1.5 1.5 0 1 1 0 3 1.5 1.5 0 0 1 0-3z"/></svg>
        <span>(512) 308 7741</span>
      </li>
      <li class="contact">
        <svg viewBox="0 0 24 24"><path d="M3 6h18v13H3zm2 2v.3l7 5.2 7-5.2V8zm0 2.8V17h14v-6.2l-7 5.2z"/></svg>
        <span>info@halverachirurgie.com</span>
      </li>
      <li class="contact">
        <svg viewBox="0 0 24 24"><path d="M12 3a9 9 0 1 0 0 18 9 9 0 0 0 0-18zm6.9 8h-3c-.1-2.2-.6-4.1-1.3-5.4A7 7 0 0 1 18.9 11zM12 5c.8 1 1.7 3.1 1.9 6h-3.8C10.3 8.1 11.2 6 12 5zM9.4 5.6C8.7 6.9 8.2 8.8 8.1 11h-3a7 7 0 0 1 4.3-5.4zM5.1 13h3c.1 2.2.6 4.1 1.3 5.4A7 7 0 0 1 5.1 13zm6.9 6c-.8-1-1.7-3.1-1.9-6h3.8c-.2 2.9-1.1 5-1.9 6zm2.6-.6c.7-1.3 1.2-3.2 1.3-5.4h3a7 7 0 0 1-4.3 5.4z"/></svg>
        <span>www.halverachirurgie.com</span>
      </li>
    </ul>
  </section>
</body>
</html>
```